Redesign Colorful Business Card

Please redesign the card attached. It is too busy. Please don't eliminate any of the words. The repetivite word "free" can be used less often.

Target Market(s)

College Students.

Contact Information for Business Card

The details listed in the attached image

Font styles to use
Sans Serif

Requirements
Must have
• A clear and simple presentation and must be attractive.

```html
<!DOCTYPE html>
<html lang="en">
<head>
<meta charset="utf-8">
<title>StudyBrisk Business Card</title>
<link rel="stylesheet" href="https://fonts.googleapis.com/css2?family=Poppins:wght@400;700&display=swap">
<style>
  :root {
    --page: #ececec;
    --card: #262626;
    --teal: #1ecbc1;
    --magenta: #f200ff;
    --ink: #ffffff;
    --badge-ink: #262626;
  }
  html, body {
    margin: 0;
    padding: 0;
    width: 1200px;
    height: 1200px;
    overflow: hidden;
    background: var(--page);
    font-family: "Poppins", Arial, sans-serif;
  }
  .card {
    position: absolute;
    left: 75px;
    top: 300px;
    width: 1050px;
    height: 600px;
    background: var(--card);
    overflow: hidden;
    box-shadow: 0 10px 30px rgba(0,0,0,0.18);
  }
  .card-bands {
    position: absolute;
    inset: 0;
  }
  .band-teal { fill: var(--teal); }
  .band-magenta { fill: var(--magenta); }
  .badge-shape { fill: var(--magenta); }
  .badge-text {
    fill: var(--badge-ink);
    font-family: "Poppins", Arial, sans-serif;
    font-weight: 700;
  }
  .brand {
    position: absolute;
    left: 70px;
    top: 268px;
    display: flex;
    align-items: center;
    gap: 16px;
  }
  .brand-mark {
    width: 34px;
    height: 34px;
    border-radius: 50%;
    background: var(--teal);
  }
  .brand-name {
    margin: 0;
    color: var(--ink);
    font-size: 46px;
    font-weight: 400;
    letter-spacing: 0.5px;
  }
  .benefits {
    position: absolute;
    left: 555px;
    top: 170px;
    width: 440px;
    margin: 0;
    padding: 0;
    list-style: none;
  }
  .benefit {
    font-size: 31px;
    font-weight: 700;
    line-height: 1.12;
    text-transform: uppercase;
    color: var(--ink);
    margin: 0 0 30px;
  }
  .benefit--accent { color: var(--teal); }
</style>
</head>
<body>
  <main class="card">
    <svg class="card-bands" width="1050" height="600" viewBox="0 0 1050 600" aria-hidden="true">
      <defs>
        <polygon id="starburst" points="70,0 51.7,21.4 49.5,49.5 21.4,51.7 0,70 -21.4,51.7 -49.5,49.5 -51.7,21.4 -70,0 -51.7,-21.4 -49.5,-49.5 -21.4,-51.7 0,-70 21.4,-51.7 49.5,-49.5 51.7,-21.4"/>
      </defs>
      <polygon class="band-teal" points="0,0 600,0 555,48 0,48"/>
      <polygon class="band-magenta" points="620,48 1050,48 1050,118 570,118"/>
      <polygon class="band-magenta" points="0,482 360,482 315,540 0,540"/>
      <polygon class="band-teal" points="400,540 1050,540 1050,600 350,600"/>

      <g class="badge" transform="translate(150 150) rotate(8)">
        <use href="#starburst" class="badge-shape"/>
        <text class="badge-text" x="0" y="11" font-size="30" text-anchor="middle">FREE</text>
      </g>
      <g class="badge" transform="translate(960 470) rotate(25) scale(0.72)">
        <use href="#starburst" class="badge-shape"/>
        <text class="badge-text" x="0" y="11" font-size="30" text-anchor="middle">FREE</text>
      </g>
    </svg>

    <div class="brand">
      <span class="brand-mark"></span>
      <h1 class="brand-name">StudyBrisk</h1>
    </div>

    <ul class="benefits">
      <li class="benefit">Cut study time<br>down by up to 50%</li>
      <li class="benefit benefit--accent">Learn a subject without having to go to class</li>
      <li class="benefit">Memorize anything<br>quickly</li>
    </ul>
  </main>
</body>
</html>
```